Home page design for a business selling commercial cleaning machines

We need a home page web design for a wholesale business selling commercial and industrial cleaning machines and spare parts. There is a huge range of products but we don't want the home page to be too cluttered and confusing.
- The design needs to be practical and functional - sharp corners, lots of white with just accents/splashes of the business colours.
- This is a link to their holding page which is very very basic - http://www.brovasco.co.nz/ - use this to get the accent colours but please use lots and lots more WHITE in the home page design! There are no colour codes available.
- The attached HPID (home page design information) is in table boxes just to see placement of information. Information in orange text. Words to go on the design in black text.
- Expected standard of design examples:
http://marnibo-flowmark.com/
http://marniboglobal.com/
http://quelvin.com/
http://www.tofmerk.wb.gs/ (different industry)
- Only use Google fonts. Non-responsive. Width 1100pixels. Header height (without nav bar) 150-160 pixels.
- Will need a PSD of the chosen homepage design (CS5 compatible)

```html
<!DOCTYPE html>
<html lang="en">
<head>
<meta charset="utf-8">
<title>Brovasco – Commercial Cleaning Machines</title>
<link rel="stylesheet" href="https://fonts.googleapis.com/css2?family=Open+Sans:wght@400;600;700&family=Source+Sans+3:wght@400;600;700&family=Arimo:wght@400;700&display=swap">
<style>
:root{
  --orange:#ef7d12;
  --orange-dark:#d96a06;
  --dark:#3b3b3b;
  --grey-bg:#f3f3f3;
  --text:#3a3a3a;
  --white:#fff;
  --machine-light:#eef1f5;
  --machine-mid:#c3ccd9;
  --machine-blue:#4f73b3;
}
*{box-sizing:border-box;margin:0;padding:0}
html,body{width:1200px;height:2387px;overflow:hidden;background:var(--white)}
body{position:relative;font-family:"Open Sans",sans-serif;color:var(--text)}
.abs{position:absolute}
a{color:inherit;text-decoration:none}

/* header */
.top-rule{left:0;top:0;width:1200px;height:7px;background:var(--orange)}
.header{left:0;top:7px;width:1200px;height:136px;background:linear-gradient(#fff,#f2f2f2)}
.brand-name{left:99px;top:34px;font-family:"Source Sans 3",sans-serif;font-weight:700;font-size:46px;letter-spacing:3px;color:#555;line-height:1}
.tagline{left:410px;top:28px;width:315px;text-align:center;font-family:"Source Sans 3",sans-serif;font-size:15px;line-height:18px;color:#555}
.tagline b{color:var(--orange);font-weight:600}
.tagline-rule{left:729px;top:30px;width:1px;height:50px;background:#bbb}
.address-box{left:745px;top:7px;width:358px;height:73px;background:var(--orange);color:#fff;font-family:"Source Sans 3",sans-serif;font-weight:600;font-size:13.5px;line-height:20px;text-align:right;padding:10px 14px}
.phone{right:97px;top:92px;font-family:"Arimo",sans-serif;font-size:31px;color:var(--orange);display:flex;align-items:center;gap:6px}
.phone svg{width:20px;height:24px}

/* nav */
.nav{left:0;top:143px;width:1200px;height:54px;background:linear-gradient(#4a4a4a,#252525);border-bottom:3px solid #1c1c1c}
.nav ul{list-style:none;display:flex;justify-content:space-between;width:1004px;margin-left:99px;height:54px;align-items:center;font-family:"Arimo",sans-serif;font-size:12.5px;color:#fff}

/* hero */
.hero{left:0;top:202px;width:1200px;height:411px}
.hero-photo{left:100px;top:274px;width:627px;height:337px;background:linear-gradient(135deg,#9a9a9a,#cfcfcf 45%,#7d7d7d);border:3px solid #d0d0d0}
.why{left:727px;top:274px;width:374px;height:337px;background:var(--dark);padding:20px 15px}
.why h2{font-family:"Source Sans 3",sans-serif;font-weight:400;font-size:23px;color:var(--orange);margin-bottom:8px}
.why ul{list-style:none;font-family:"Arimo",sans-serif;font-size:11.5px;color:#fff}
.why li{height:30px;line-height:30px;padding-left:15px;position:relative}
.why li:before{content:"";position:absolute;left:2px;top:12px;border-left:5px solid var(--orange);border-top:3px solid transparent;border-bottom:3px solid transparent}

/* product cards */
.section-title{left:99px;top:664px;font-family:"Source Sans 3",sans-serif;font-weight:600;font-size:18px;letter-spacing:1px;color:#333}
.card{top:707px;width:202px;height:229px;border:1px solid #ddd;border-radius:6px;background:#fff;overflow:hidden;box-shadow:0 1px 3px rgba(0,0,0,.12)}
.card-photo{height:128px;margin:10px 12px 0;border-radius:3px;background:linear-gradient(180deg,var(--machine-light) 0%,var(--machine-mid) 62%,var(--machine-blue) 100%)}
.card-photo.sweeper{background:linear-gradient(160deg,var(--machine-light) 0%,#dde2ea 45%,#8d98a8 80%,#3f4652 100%)}
.card-label{margin-top:8px;height:28px;line-height:28px;text-align:center;font-family:"Source Sans 3",sans-serif;font-weight:600;font-size:13.5px;color:var(--orange);background:#f4f4f4}
.card-more{position:absolute;bottom:0;left:0;right:0;height:50px;line-height:50px;background:#6e6e6e;color:#fff;text-align:center;font-family:"Arimo",sans-serif;font-size:13px;text-decoration:underline}

/* browse bar */
.browse{left:102px;top:972px;width:1002px;height:86px;border:1px solid #ddd;border-radius:6px;background:linear-gradient(#fff,#f4f4f4);box-shadow:0 1px 3px rgba(0,0,0,.1)}
.browse-tag{left:0;top:0;width:122px;height:84px;background:var(--orange);color:#fff;font-family:"Source Sans 3",sans-serif;font-weight:700;font-size:24px;line-height:84px;padding-left:12px;border-radius:5px 0 0 5px}
.browse-tag:after{content:"";position:absolute;right:-14px;top:28px;border-left:14px solid var(--orange);border-top:14px solid transparent;border-bottom:14px solid transparent}
.browse-text{left:140px;top:14px;width:850px;text-align:center;font-family:"Source Sans 3",sans-serif;font-size:19px;line-height:30px;color:#666}
.browse-text b{color:#222;font-weight:600}
.dash-rule{left:100px;top:1089px;width:1002px;border-top:1px dashed #c4c4c4}

/* feature boxes */
.feature{top:1159px;width:300px;height:210px;border:1px solid #ddd;border-radius:6px;background:#fff;box-shadow:0 1px 3px rgba(0,0,0,.12);overflow:hidden}
.feature h3{height:84px;display:flex;align-items:center;justify-content:center;text-align:center;font-family:"Source Sans 3",sans-serif;font-weight:600;font-size:18px;line-height:24px;letter-spacing:.8px;color:#333}
.feature-photo{position:absolute;left:4px;right:4px;bottom:4px;height:122px}
.feature-btn{position:absolute;left:50%;transform:translateX(-50%);bottom:14px;background:var(--orange);color:#fff;font-family:"Source Sans 3",sans-serif;font-weight:600;font-size:13px;padding:6px 16px;border-radius:5px}

/* contact form */
.form-band{left:0;top:1388px;width:1200px;height:565px;background:var(--grey-bg)}
.form-title{left:0;top:1487px;width:1200px;text-align:center;font-family:"Source Sans 3",sans-serif;font-weight:600;font-size:24px;letter-spacing:1px;color:#555}
.form-sub{left:0;top:1522px;width:1200px;text-align:center;font-family:"Source Sans 3",sans-serif;font-weight:600;font-size:19px;letter-spacing:.5px;color:#555}
.form-rule{left:100px;top:1571px;width:992px;border-top:1px solid #bdbdbd}
.field{width:329px;height:42px;border:1px solid #c7c7c7;border-radius:5px;background:#fff;font-family:"Arimo",sans-serif;font-size:13px;color:#b0b0b0;padding:0 12px;line-height:40px}
.send{left:490px;top:1824px;width:202px;height:48px;background:var(--orange);border:1px solid var(--orange-dark);border-radius:5px;color:#fff;font-family:"Arimo",sans-serif;font-size:21px;text-align:center;line-height:46px}

/* brands */
.brands{left:62px;top:2002px;width:1078px;height:99px;border:1px solid #e0e0e0;border-radius:6px;background:#f7f7f7}
.brands-title{left:0;top:2006px;width:1200px;text-align:center;font-family:"Source Sans 3",sans-serif;font-weight:600;font-size:21px;letter-spacing:1px;color:#333}
.brand-strip{left:103px;top:2044px;width:998px;height:38px;display:flex;gap:2px}
.brand{flex:1;background:#fff;border:1px solid #ddd;display:flex;align-items:center;justify-content:center;font-family:"Source Sans 3",sans-serif;font-weight:700;font-size:17px;color:#555}
.arrow{top:2050px;width:16px;height:28px}

/* footer */
.footer{left:0;top:2145px;width:1200px;height:242px;background:#474747}
.footer-map{left:99px;top:2168px;width:350px;height:194px;background:linear-gradient(160deg,#cfe0f2,#b8d2ee);border:4px solid #fff}
.footer-links{list-style:none;font-family:"Arimo",sans-serif;font-size:12px;color:#fff}
.footer-links li{height:24px;padding-left:13px;position:relative}
.footer-links li:before{content:"";position:absolute;left:0;top:4px;border-left:5px solid var(--orange);border-top:3px solid transparent;border-bottom:3px solid transparent}
.footer-brand{left:855px;top:2214px;width:248px;text-align:right;font-family:"Source Sans 3",sans-serif;font-weight:700;font-size:36px;letter-spacing:3px;color:#bdbdbd}
.socials{left:885px;top:2281px;display:flex;gap:10px}
.socials span{width:32px;height:32px;border-radius:50%;background:#fff;display:block}
.bottom-rule{left:0;top:2381px;width:1200px;height:6px;background:var(--orange)}
</style>
</head>
<body>

<div class="abs top-rule"></div>
<header class="abs header"></header>
<div class="abs brand-name">BROVASCO</div>
<p class="abs tagline"><b>Wholesale importer &amp; distributor of quality Italian industrial,</b> commercial &amp; domestic cleaning machines &amp; accessories</p>
<div class="abs tagline-rule"></div>
<div class="abs address-box">2 / 48 Tarvin St, Otaroa (office). Open to the public.<br>Head office Rimu Coast | Distributors NZ wide</div>
<div class="abs phone">
  <svg viewBox="0 0 20 24"><path d="M5 1l3 5-2 2c1 4 3 7 6 9l2-2 5 3-2 4C9 22 2 13 1 4z" fill="#444"/></svg>
  04 555 0182
</div>

<nav class="abs nav">
  <ul>
    <li>Home</li><li>About</li><li>Water blasters</li><li>Drain cleaners</li><li>Custom machines</li><li>Vacuum Cleaners</li><li>Spare Parts</li><li>PTO machines</li><li>FAQ</li><li>Quote</li><li>Contact</li>
  </ul>
</nav>

<svg class="abs hero" viewBox="0 0 1200 411" preserveAspectRatio="none">
  <rect width="1200" height="411" fill="#ef7d12"/>
  <path d="M0 411 L0 395 Q120 330 300 345 L900 345 Q1080 330 1200 395 L1200 411 Z" fill="#fff"/>
</svg>
<div class="abs hero-photo" role="img" aria-label="Operator driving a floor scrubber in an industrial plant room"></div>
<aside class="abs why">
  <h2>Why Choose Brovasco?</h2>
  <ul>
    <li>High quality Italian cleaning machines</li>
    <li>Wide range of brands and models</li>
    <li>Specialist knowledge &amp; expert advice</li>
    <li>Cost of machines – more affordable for top quality</li>
    <li>Able to service and repair all types of cleaning machines</li>
    <li>Huge range of affordable spare parts</li>
    <li>Distributors nationwide offering excellent sales &amp; service</li>
    <li>Great family business with excellent customer service for</li>
    <li>over 24 years!</li>
  </ul>
</aside>

<h2 class="abs section-title">HUGE RANGE OF QUALITY CLEANING MACHINES...</h2>
<div class="abs card" style="left:99px"><div class="card-photo sweeper" role="img" aria-label="White and grey walk-behind sweeper machine"></div><div class="card-label">WATER BLASTERS</div><a class="card-more">MORE INFORMATION</a></div>
<div class="abs card" style="left:374px"><div class="card-photo" role="img" aria-label="Three floor polishing machines with blue bases"></div><div class="card-label">DRAIN CLEANERS</div><a class="card-more">MORE INFORMATION</a></div>
<div class="abs card" style="left:638px"><div class="card-photo sweeper" role="img" aria-label="White and grey walk-behind sweeper machine"></div><div class="card-label">CUSTOM MACHINES</div><a class="card-more">MORE INFORMATION</a></div>
<div class="abs card" style="left:899px"><div class="card-photo" role="img" aria-label="Three floor polishing machines with blue bases"></div><div class="card-label">VACCUM CLEANERS</div><a class="card-more">MORE INFORMATION</a></div>

<div class="abs browse">
  <div class="abs browse-tag">Browse</div>
  <p class="abs browse-text"><b>Products</b>, <b>Add any item</b> to a quote request form or <b>Give us a call</b> for more information.<br>Not sure what you need? Contact us for expert advice – <b>we’re happy to assist!</b></p>
</div>
<div class="abs dash-rule"></div>

<div class="abs feature" style="left:124px">
  <h3>HUGE RANGE OF QUALITY<br>CLEANING MACHINES</h3>
  <div class="feature-photo" role="img" aria-label="Cleaning machines lined up on a showroom floor" style="background:linear-gradient(135deg,#5a6a80,#9aa6b4 50%,#3d4a5c)"></div>
  <a class="feature-btn">All Products</a>
</div>
<div class="abs feature" style="left:450px">
  <h3>NATIONWIDE DISTRIBUTORS<br>FOR SALES &amp; SERVICING</h3>
  <div class="feature-photo" role="img" aria-label="Map of New Zealand" style="background:linear-gradient(135deg,#a9c8ee,#c6dbf4)"></div>
  <a class="feature-btn">Contact</a>
</div>
<div class="abs feature" style="left:772px">
  <h3>COMPREHENSIVE RANGE<br>OF SPARE PARTS</h3>
  <div class="feature-photo" role="img" aria-label="Worker in a spare parts warehouse" style="background:linear-gradient(135deg,#6f6a5c,#b9b1a0 50%,#5a5448)"></div>
  <a class="feature-btn">Spare Parts</a>
</div>

<section class="abs form-band"></section>
<h2 class="abs form-title">WOULD YOU LIKE A BROVASCO REPRESENTATIVE TO CONTACT YOU?</h2>
<p class="abs form-sub">Please fill in the form and we’ll be in touch very soon...</p>
<div class="abs form-rule"></div>
<div class="abs field" style="left:231px;top:1619px">First Name:</div>
<div class="abs field" style="left:602px;top:1619px">Last Name:</div>
<div class="abs field" style="left:231px;top:1682px">Contact:</div>
<div class="abs field" style="left:602px;top:1682px">Email Address:</div>
<div class="abs field" style="left:231px;top:1752px">Area you live in ?</div>
<div class="abs field" style="left:602px;top:1752px">Any further details:</div>
<div class="abs send">SEND NOW !</div>

<div class="abs brands"></div>
<h2 class="abs brands-title">BRANDS</h2>
<svg class="abs arrow" style="left:70px" viewBox="0 0 16 28"><path d="M13 2L3 14l10 12" fill="none" stroke="#999" stroke-width="4"/></svg>
<svg class="abs arrow" style="left:1114px" viewBox="0 0 16 28"><path d="M3 2l10 12L3 26" fill="none" stroke="#999" stroke-width="4"/></svg>
<div class="abs brand-strip">
  <div class="brand">Carvetti</div>
  <div class="brand">Falcor</div>
  <div class="brand">Jetstrom</div>
  <div class="brand">Idrovera</div>
  <div class="brand">Orbitek</div>
  <div class="brand">Pompatec Group</div>
  <div class="brand">Valvex</div>
</div>

<footer class="abs footer"></footer>
<div class="abs footer-map" role="img" aria-label="Map of New Zealand and Australia"></div>
<ul class="abs footer-links" style="left:503px;top:2187px">
  <li>Home</li><li>About</li><li>Meet the Team</li><li>Testimonials</li><li>FAQ</li><li>Quote</li><li>Contact/Map</li>
</ul>
<ul class="abs footer-links" style="left:676px;top:2187px">
  <li>Water blasters</li><li>Drain cleaners</li><li>Custom machines</li><li>Vacuum Cleaners</li><li>Pumps high pressure</li><li>Spare Parts</li><li>PTO machines</li>
</ul>
<div class="abs footer-brand">BROVASCO</div>
<div class="abs socials"><span></span><span></span><span></span><span></span><span style="position:relative"><svg viewBox="0 0 32 32" width="32" height="32"><path d="M16 8v16M8 16h16" stroke="#474747" stroke-width="4"/></svg></span></div>
<div class="abs bottom-rule"></div>

</body>
</html>
```